Progressive and innovative Russian bank needs Landing Page for debit card with APR profit 9%

We need a web-design of the Landing Page for our new online retail financial service for Russian customers, debit card, named 'Harvest Card'. Harvest Card - is the debit stand-alone card (debit card not linked to a term deposit). Clients is getting profit (% on it's cash balance) depending on amount of cash:
- up to 30000₽ - 0%, 30000.01-700000₽ - 9% APR, more 700000₽ - 5% APR
- up to 1000$/€ - 0%, 1000-15000$/€ - 4% APR, more 15000$/€ - 2% APR
Clients can use the card as usual debit card for purchases in shops and payments (via internet too), etc. Traffic to the Landing Page come from ads in Searlo and Vokrum (Russian Searlo). We would like to see designs that use our brand colors and logo. The final design should follow brand limitations. Files in psd format.
Северный Вековой Банк

Reason: Thank you all. Our task was to make design of Landing page of the product. Majority of designs was the design of corporate site webpage. Please refine on your design.

```html
<!DOCTYPE html>
<html lang="ru">
<head>
<meta charset="utf-8">
<title>Harvest Card — Северный Вековой Банк</title>
<link href="https://fonts.googleapis.com/css2?family=Roboto+Condensed:wght@400;700&family=Roboto:wght@400;700&display=swap" rel="stylesheet">
<style>
:root{
  --blue:#0b4f94;
  --lime:#c5d12b;
  --ink:#222;
  --grey:#555;
  --dark:#2e2a29;
  --darker:#3a3534;
  --bar:#3b3635;
  --chip:#6b6564;
  --arrow:#d6d6d6;
  --white:#fff;
}
*{box-sizing:border-box;margin:0;padding:0}
html,body{width:1200px;height:2930px;overflow:hidden;background:var(--white)}
body{position:relative;font-family:"Roboto",Arial,sans-serif;color:var(--ink)}
.abs{position:absolute}

.topbar{left:0;top:0;width:1200px;height:49px;background:var(--blue)}
.topbar .welcome{left:95px;top:16px;color:var(--white);font-size:14px}
.topbar .search{left:1019px;top:0;width:181px;height:49px;background:var(--lime);display:flex;align-items:center;justify-content:center}

.header{left:0;top:49px;width:1200px;height:117px;background:var(--white)}
.brand{left:95px;top:24px;display:flex;align-items:center;gap:14px}
.brand-name{color:var(--blue);font-size:17px;line-height:20px}
.brand-mark{width:22px;height:22px;background:var(--lime)}
.nav{right:95px;top:50px;display:flex;gap:30px;font-family:"Roboto Condensed",sans-serif;font-size:16px;color:var(--ink)}
.nav .active{color:var(--blue);font-weight:700}

.hero{left:0;top:166px;width:1200px;height:440px;background:linear-gradient(100deg,#b9a89a 0%,#d8ccbf 40%,#c9bdb1 70%,#a89c91 100%)}
.hero-tag{background:var(--blue);color:var(--white);font-family:"Roboto Condensed",sans-serif;text-transform:uppercase;text-align:center;border:3px solid var(--white);white-space:nowrap}
.hero-tag.small{left:706px;top:286px;width:233px;height:54px;font-size:34px;line-height:48px}
.hero-tag.big{left:618px;top:349px;width:487px;height:83px;font-size:46px;line-height:77px;font-weight:700}
.btn-trap{color:var(--white);font-family:"Roboto Condensed",sans-serif;font-weight:700;text-transform:uppercase;background:var(--blue);clip-path:polygon(0 0,100% 0,92% 100%,8% 100%);text-align:center;white-space:nowrap}
.hero-read{left:755px;top:442px;width:200px;height:49px;font-size:24px;line-height:49px}

.section-title{border:2px solid #333;font-family:"Roboto Condensed",sans-serif;font-weight:700;font-size:24px;text-align:center;text-transform:uppercase;letter-spacing:.5px;white-space:nowrap}
.products-title{left:474px;top:679px;width:252px;height:54px;line-height:50px;color:#333}
.intro{left:130px;top:782px;width:940px;text-align:center;font-size:13px;line-height:21px;color:var(--grey)}
.product-a{left:196px;top:885px;width:376px;height:232px;background:linear-gradient(135deg,#dfe9f4,#8faecd)}
.product-b{left:628px;top:885px;width:376px;height:232px;background:linear-gradient(135deg,#1c1e22,#3d4f6e 60%,#b89b86)}
.view-more{left:494px;top:1215px;width:212px;height:53px;font-size:24px;line-height:53px}

.benefits{left:0;top:1373px;width:1200px;height:636px;background:linear-gradient(180deg,#2d2d2f,#454547 50%,#2a2a2c)}
.benefits-title{left:428px;top:1459px;width:344px;height:54px;line-height:50px;color:var(--white);border-color:var(--white)}
.benefit{width:320px;color:var(--white)}
.benefit .head{display:flex;align-items:center;gap:16px;height:44px}
.benefit .num{flex:none;width:44px;height:44px;background:var(--white);color:#333;font-family:"Roboto Condensed",sans-serif;font-weight:700;font-size:32px;text-align:center;line-height:44px}
.benefit h3{font-family:"Roboto Condensed",sans-serif;font-size:21px;font-weight:700;text-transform:uppercase;position:relative;white-space:nowrap}
.benefit h3::after{content:"";position:absolute;left:0;bottom:-12px;width:44px;height:2px;background:var(--white)}
.benefit p{margin-top:20px;font-size:13px;line-height:20px;color:#e8e8e8;height:60px}
.benefit .more{margin-top:10px;font-family:"Roboto Condensed",sans-serif;font-weight:700;font-size:15px;text-transform:uppercase}

.testi-title{left:469px;top:2082px;width:259px;height:54px;line-height:50px;color:#333}
.portrait{left:95px;top:2197px;width:286px;height:220px;background:linear-gradient(135deg,#cfd3d6,#9aa1a6 60%,#b6a48e)}
.testi-name{left:423px;top:2228px;font-family:"Roboto Condensed",sans-serif;font-weight:700;font-size:21px;color:#333}
.testi-name::after{content:"";display:block;width:80px;height:2px;background:#333;margin-top:10px}
.testi-text{left:423px;top:2280px;width:520px;font-size:13px;line-height:20px;color:var(--grey)}
.arrows{left:1007px;top:2200px;display:flex;gap:6px}
.arrows span{width:44px;height:41px;background:var(--arrow);display:flex;align-items:center;justify-content:center}

.footer{left:0;top:2476px;width:1200px;height:366px;background:var(--dark)}
.fcol{top:2476px;width:338px;height:317px;background:var(--darker);color:var(--white);text-align:center}
.fcol .fhead{height:102px;line-height:102px;font-family:"Roboto Condensed",sans-serif;font-weight:700;font-size:26px;text-transform:uppercase;white-space:nowrap}
.fcol .rule{width:44px;height:2px;background:var(--white);margin:28px auto 16px}
.fcol p{font-size:13px;line-height:20px;padding:0 34px;color:#eee}
.fcol .fbtn{display:inline-block;margin-top:26px;border:2px solid var(--white);width:134px;height:38px;line-height:34px;font-family:"Roboto Condensed",sans-serif;font-weight:700;font-size:14px}
.signup{display:flex;justify-content:center;gap:4px;margin:16px 0 14px}
.signup .field{width:184px;height:38px;border:2px solid var(--white)}
.signup .send{width:80px;height:38px;background:#e6e6e6;color:#333;font-family:"Roboto Condensed",sans-serif;font-weight:700;font-size:16px;line-height:38px}

.bottombar{left:0;top:2842px;width:1200px;height:88px;background:var(--bar);color:#e6e6e6;font-size:13px}
.copyright{left:95px;top:36px}
.flinks{left:448px;top:36px;display:flex;gap:22px}
.social{left:920px;top:30px;display:flex;gap:10px}
.social span{width:26px;height:26px;background:var(--chip)}
</style>
</head>
<body>

<div class="abs topbar">
  <div class="abs welcome">Welcome to our site visitors</div>
  <div class="abs search">
    <svg width="16" height="16" viewBox="0 0 16 16" aria-label="Search"><circle cx="6.5" cy="6.5" r="4.5" fill="none" stroke="#fff" stroke-width="2"/><line x1="10" y1="10" x2="14" y2="14" stroke="#fff" stroke-width="2"/></svg>
  </div>
</div>

<header class="abs header">
  <div class="abs brand">
    <div class="brand-name">Северный<br>Вековой<br>Банк</div>
    <div class="brand-mark"></div>
  </div>
  <nav class="abs nav">
    <span class="active">HOME</span><span>ABOUT US</span><span>OUR SERVICES</span><span>BLOG</span><span>FAQs</span><span>CONTACT US</span>
  </nav>
</header>

<section class="abs hero" role="img" aria-label="Couple on a sofa paying online with a debit card on a laptop"></section>
<div class="abs hero-tag small">Harvest Card</div>
<div class="abs hero-tag big">Earn up to 9% APR</div>
<div class="abs btn-trap hero-read">Get card</div>

<h2 class="abs section-title products-title">Harvest Card</h2>
<p class="abs intro">A stand-alone debit card, not linked to a term deposit. Earn interest on your cash balance every month and use it as a usual debit card: pay in shops, online and for everyday services. Balances in rubles earn up to 9% APR, balances in dollars and euros earn up to 4% APR.</p>
<div class="abs product-a" role="img" aria-label="Hands typing on a laptop while holding a debit card for an online payment"></div>
<div class="abs product-b" role="img" aria-label="Debit card inserted into a payment terminal in a shop"></div>
<div class="abs btn-trap view-more">Order card</div>

<section class="abs benefits" role="img" aria-label="Dark aerial view of a city"></section>
<h2 class="abs section-title benefits-title">What you get from us</h2>

<div class="abs benefit" style="left:95px;top:1576px"><div class="head"><div class="num">1</div><h3>0% up to 30 000 ₽</h3></div><p>A ruble balance up to 30 000 ₽ is kept free of charge and always available for your everyday purchases and payments</p><div class="more">Read more</div></div>
<div class="abs benefit" style="left:450px;top:1576px"><div class="head"><div class="num">2</div><h3>9% APR on rubles</h3></div><p>Every ruble from 30 000.01 ₽ to 700 000 ₽ earns 9% APR on your cash balance, paid to the card with no deposit needed</p><div class="more">Read more</div></div>
<div class="abs benefit" style="left:804px;top:1576px"><div class="head"><div class="num">3</div><h3>5% APR over 700 000 ₽</h3></div><p>Larger ruble balances above 700 000 ₽ keep growing at 5% APR while your money stays free to spend at any time</p><div class="more">Read more</div></div>
<div class="abs benefit" style="left:95px;top:1784px"><div class="head"><div class="num">4</div><h3>4% APR on $ and €</h3></div><p>Balances from 1 000 to 15 000 $/€ earn 4% APR; a balance up to 1 000 $/€ is kept at 0% and stays ready to use</p><div class="more">Read more</div></div>
<div class="abs benefit" style="left:450px;top:1784px"><div class="head"><div class="num">5</div><h3>2% APR over 15 000 $/€</h3></div><p>Dollar and euro balances above 15 000 $/€ earn 2% APR, so savings in every currency keep working for you</p><div class="more">Read more</div></div>
<div class="abs benefit" style="left:804px;top:1784px"><div class="head"><div class="num">6</div><h3>Pay anywhere</h3></div><p>Use Harvest Card as a usual debit card in shops, on the internet and for bills, with interest still paid on the balance</p><div class="more">Read more</div></div>

<h2 class="abs section-title testi-title">What they says</h2>
<div class="abs portrait" role="img" aria-label="Portrait of a customer in a beige coat and scarf"></div>
<div class="abs testi-name">JOHN DOE, 25 YO</div>
<p class="abs testi-text">I pay with Harvest Card in shops and online every day, and my balance still earns 9% APR. No deposit, no extra accounts — the interest simply arrives on the card every month .....</p>
<div class="abs arrows">
  <span><svg width="16" height="22" viewBox="0 0 16 22"><polyline points="12,2 3,11 12,20" fill="none" stroke="#fff" stroke-width="3"/></svg></span>
  <span><svg width="16" height="22" viewBox="0 0 16 22"><polyline points="4,2 13,11 4,20" fill="none" stroke="#fff" stroke-width="3"/></svg></span>
</div>

<footer class="abs footer"></footer>
<div class="abs fcol" style="left:95px">
  <div class="fhead" style="background:var(--blue)">About us</div>
  <div class="rule"></div>
  <p>Северный Вековой Банк offers simple online banking for Russian customers with cards that earn on every balance</p>
  <div class="fbtn">READ MORE</div>
</div>
<div class="abs fcol" style="left:433px">
  <div class="fhead" style="background:var(--lime)">Company address</div>
  <div class="rule"></div>
  <p>Find our offices and service points, opening hours and contacts for Harvest Card holders across Russia</p>
  <div class="fbtn">READ MORE</div>
</div>
<div class="abs fcol" style="left:771px">
  <div class="fhead" style="background:var(--blue)">Newsletter</div>
  <div class="rule"></div>
  <p>Get news on Harvest Card rates</p>
  <div class="signup"><div class="field"></div><div class="send">SEND</div></div>
  <p>We will tell you first when APR rates and card offers change for your balance</p>
</div>

<div class="abs bottombar">
  <div class="abs copyright">© 2014 <b>YOUR COMPANY</b>. ALL RIGHTS RESERVED.</div>
  <div class="abs flinks"><span>ABOUT US</span><span>TERM AND USE</span><span>PRIVACY POLICY</span><span>FAQS</span><span>CONTACT US</span></div>
  <div class="abs social" aria-label="Social links"><span></span><span></span><span></span><span></span><span></span></div>
</div>

</body>
</html>
```